Designing business cards for my start-up business

The company is called Velloran. We are a start-up tech data company based in Guernsey, Channel Islands. We want the business cards to look clean, fresh and innovative, just what a tech company should be. We do not want the business cards to look corporate or too official such as a bank. I would like the front of the business card to have our logo and the tag line of "bridging bright minds". On the back will be our contact details, emails etc. However I am open to your ideas and suggestions. I have provided all our logos and a word doc of all our contact details. There are 4 directors of the business, so I want 4 versions of the same design.

Target Market(s)

Our clients are businesses of all industries. Its a broad target market.

Industry/Entity Type

Information Technology

Contact Information for Business Card

I have attached a word doc called "Business Cards info" which gives all contact details of the 4 employees for the company.

Requirements
Must have
• We must have our logo and the tag line of "bridging bright minds". This could on the front of the card and then the individuals contact details on the back. Other than that, I'm happy for the designers to come up with ideas/styles.
Nice to have
• N/A
Should not have
• I don't want the cards to look too formal or corporate. As mentioned, we are a tech start-up so we want to look innovative.

```html
<!DOCTYPE html>
<html lang="en">
<head>
<meta charset="utf-8">
<title>Velloran business card</title>
<link rel="stylesheet" href="https://fonts.googleapis.com/css2?family=Roboto:wght@400&family=Open+Sans:wght@600&display=swap">
<style>
  :root {
    --backdrop: #e9e6e1;
    --card: #ffffff;
    --ink: #111111;
    --muted: #555555;
    --accent: #f15a36;
    --accent-deep: #b8321f;
    --silver-light: #f4f4f4;
    --silver-mid: #d9d9d9;
    --silver-dark: #a9a9a9;
  }
  html, body {
    margin: 0;
    padding: 0;
    width: 1000px;
    height: 1200px;
    overflow: hidden;
    background: var(--backdrop);
  }
  .canvas {
    position: relative;
    width: 1000px;
    height: 1200px;
  }
  .card {
    position: absolute;
    left: 130px;
    width: 736px;
    height: 485px;
    background: var(--card);
    box-shadow: 0 4px 10px rgba(0,0,0,0.25);
    overflow: hidden;
  }
  .card--front { top: 83px; }
  .card--back { top: 634px; }
  .card__art {
    position: absolute;
    inset: 0;
    width: 736px;
    height: 485px;
  }
  .identity {
    position: absolute;
    left: 48px;
    top: 72px;
    font-family: "Roboto", Arial, sans-serif;
  }
  .identity__name {
    margin: 0;
    font-size: 36px;
    font-weight: 400;
    color: var(--ink);
    line-height: 1;
    letter-spacing: -0.3px;
  }
  .identity__role {
    margin: 6px 0 0;
    font-size: 19px;
    font-weight: 400;
    color: var(--accent);
    line-height: 1;
  }
  .contacts {
    position: absolute;
    left: 48px;
    top: 176px;
    margin: 0;
    padding: 0;
    list-style: none;
    font-family: "Roboto", Arial, sans-serif;
    font-size: 19px;
    color: var(--ink);
  }
  .contacts__item {
    display: flex;
    align-items: center;
    height: 26px;
  }
  .contacts__icon {
    width: 18px;
    height: 18px;
    margin-right: 10px;
    flex: none;
  }
  .brand {
    position: absolute;
    left: 0;
    right: 0;
    top: 190px;
    display: flex;
    justify-content: center;
    align-items: center;
    gap: 14px;
  }
  .brand__square {
    width: 34px;
    height: 34px;
    background: var(--accent);
  }
  .brand__name {
    font-family: "Open Sans", Arial, sans-serif;
    font-weight: 600;
    font-size: 46px;
    color: var(--accent);
    line-height: 1;
  }
  .tagline {
    position: absolute;
    left: 0;
    right: 0;
    top: 326px;
    margin: 0;
    text-align: center;
    font-family: "Roboto", Arial, sans-serif;
    font-weight: 400;
    font-size: 19px;
    color: var(--muted);
    line-height: 1;
  }
</style>
</head>
<body>
<main class="canvas">

  <section class="card card--front">
    <svg class="card__art" viewBox="0 0 736 485" aria-hidden="true">
      <defs>
        <linearGradient id="silverSheet" x1="0" y1="0" x2="1" y2="1">
          <stop offset="0" stop-color="var(--silver-light)"/>
          <stop offset="0.55" stop-color="#ececec"/>
          <stop offset="0.78" stop-color="var(--silver-mid)"/>
          <stop offset="0.9" stop-color="var(--silver-dark)"/>
          <stop offset="1" stop-color="#e6e6e6"/>
        </linearGradient>
        <linearGradient id="accentField" x1="0" y1="1" x2="1" y2="0">
          <stop offset="0" stop-color="var(--accent-deep)"/>
          <stop offset="0.35" stop-color="var(--accent)"/>
          <stop offset="1" stop-color="var(--accent)"/>
        </linearGradient>
      </defs>
      <polygon points="657,0 736,0 736,485 175,485" fill="url(#accentField)"/>
      <polygon points="0,0 657,0 175,485 0,485" fill="url(#silverSheet)"/>
    </svg>

    <div class="identity">
      <h1 class="identity__name">Elise Durand</h1>
      <p class="identity__role">Director</p>
    </div>

    <ul class="contacts">
      <li class="contacts__item">
        <svg class="contacts__icon" viewBox="0 0 18 18" aria-hidden="true">
          <path d="M2 7c0-3 3-4 7-4s7 1 7 4l-3 1-1-2H6L5 8z" fill="var(--accent)"/>
          <path d="M4 9h10l1 6H3z" fill="var(--accent)"/>
          <circle cx="9" cy="12" r="1.8" fill="#fff"/>
        </svg>
        <span>+44 7700 900 318</span>
      </li>
      <li class="contacts__item">
        <svg class="contacts__icon" viewBox="0 0 18 18" aria-hidden="true">
          <rect x="1" y="4" width="16" height="11" fill="var(--accent)"/>
          <path d="M1.5 4.5 9 10.5l7.5-6M1.5 14.5l5.5-5M16.5 14.5l-5.5-5" fill="none" stroke="#fff" stroke-width="1.3"/>
        </svg>
        <span>Elise.Durand@velloran.gg</span>
      </li>
      <li class="contacts__item">
        <svg class="contacts__icon" viewBox="0 0 18 18" aria-hidden="true">
          <circle cx="9" cy="9" r="7.5" fill="var(--accent)"/>
          <path d="M1.5 9h15M9 1.5v15M9 1.5c-4 4-4 11 0 15M9 1.5c4 4 4 11 0 15" fill="none" stroke="#fff" stroke-width="1.1"/>
        </svg>
        <span>www.velloran.gg</span>
      </li>
    </ul>
  </section>

  <section class="card card--back">
    <div class="brand">
      <span class="brand__square"></span>
      <span class="brand__name">Velloran</span>
    </div>
    <p class="tagline">bridging bright minds</p>
  </section>

</main>
</body>
</html>
```